VoltaRush Product Logo and Package

***Update*** Please you the text from the attached images on the product design.
Suggested Text:
Logo - VoltaRush
Title - Beta-hydroxybutyrates (BHB)Â Ketone Supplement
Beta-hydroxybutyrates (BHB)Â Ketone Supplement
Beta-hydroxybutyrates (BHB)Â Exogenous Ketones
Beta-hydroxybutyrates (BHB)Â Salts
Instant Ketones
3) Flavor - Orange Mango
4) Servings - 30 Servings 12g BHB Per Serving
5) Seals - Made in USA, FDA Certified Facility, GF (gluten Free), Dairy Free, Keto Friendly, Vegan Friendly, Non-GMO, Naturally Flavored, No Preservatives
6) Uses - Energy, Mental Clarity, Fat Loss, Muscle Strength, Appetite Suppression, Mood Management
7) Big Benefit - Formulated To Induce Rapid Ketosis.
Enjoy the benefits of Ketosis anytime!
50% More Servings Compared To Other Leading Brands!
I would like a logo and package designed for a supplement.
It is a powdered supplement that can be packaged in a plastic jar (8-16 oz) or a bag.
We will also be adding additional products to this line and would like the branding to scale.
The product is packaged in a 16 oz tub.
Product Title: Beta-hydroxybutyrates (BHB) Ketone Supplement
Brand Name: VoltaRush (I'd like the logo image to share the E)
Updates
Project Deadline Extended
Reason: I'd like to attract more designers and give them more time to submit briefs.
Target Market(s)
Health and Fitness Enthusiasts. Specifically those interested in a Ketogenic Lifestyle.
Industry/Entity Type
Health And Wellness
Requirements
Must have
- Modern, trendy, design.
- Bold colors and fonts.
- Professional but trendy.
- I would like to see Red and Black as the colors used.
Should not have
- Standard, corporate feel.
- Must be fun, engaging, and exciting.

```html
<!DOCTYPE html>
<html lang="en">
<head>
<meta charset="utf-8">
<title>VoltaRush BHB Ketone Supplement – Label Options</title>
<link href="https://fonts.googleapis.com/css2?family=Montserrat:wght@600&family=Source+Sans+3:wght@600;700;800&family=Oswald:wght@500&display=swap" rel="stylesheet">
<style>
  :root {
    --page: #f3f3f3;
    --black: #0b0b0b;
    --red: #ec1c24;
    --orange: #f7941d;
    --yellow: #ffe600;
    --grey-bar: #9a9a9a;
    --grey-bar-light: #c9c9c9;
    --ink: #1a1a1a;
    --white: #ffffff;
    --silver: #cfcfcf;
  }
  html, body {
    margin: 0;
    width: 1200px;
    height: 728px;
    overflow: hidden;
    background: var(--page);
  }
  .canvas {
    position: relative;
    width: 1200px;
    height: 728px;
  }
  .label {
    position: absolute;
    top: 130px;
    width: 340px;
    height: 470px;
    overflow: hidden;
    background: var(--black);
    box-shadow: 0 10px 30px rgba(0,0,0,.18);
    font-family: "Source Sans 3", Arial, sans-serif;
  }
  .label--inline { left: 130px; }
  .label--stacked { left: 730px; }

  .label__stripe {
    position: absolute;
    left: 0; right: 0;
    top: 30px;
    height: 16px;
    background: linear-gradient(90deg, var(--red) 0%, var(--orange) 30%, var(--yellow) 50%, var(--orange) 70%, var(--red) 100%);
  }
  .label__lower {
    position: absolute;
    left: 0; right: 0;
    top: 280px;
    bottom: 0;
    background:
      radial-gradient(ellipse 55% 110% at 50% 100%, var(--yellow) 0%, var(--orange) 45%, rgba(247,148,29,0) 80%),
      linear-gradient(90deg, var(--red) 0%, var(--orange) 35%, var(--orange) 65%, var(--red) 100%);
  }
  .brand {
    position: absolute;
    left: 0; right: 0;
    text-align: center;
    font-family: "Montserrat", Arial, sans-serif;
    font-weight: 600;
    margin: 0;
  }
  .label--inline .brand {
    top: 136px;
    font-size: 38px;
    color: var(--white);
    letter-spacing: 1px;
  }
  .label--stacked .brand {
    top: 118px;
    font-size: 52px;
    color: var(--silver);
    letter-spacing: 1px;
  }
  .compound {
    position: absolute;
    left: 45px;
    width: 251px;
    top: 263px;
    height: 33px;
    line-height: 33px;
    text-align: center;
    background: linear-gradient(180deg, var(--grey-bar-light), var(--grey-bar));
    color: var(--ink);
    font-weight: 600;
    font-size: 17px;
  }
  .title {
    position: absolute;
    left: 0; right: 0;
    top: 308px;
    text-align: center;
    font-weight: 800;
    font-size: 22px;
    color: var(--ink);
    margin: 0;
  }
  .category {
    position: absolute;
    left: 61px;
    width: 217px;
    top: 340px;
    height: 27px;
    line-height: 26px;
    box-sizing: border-box;
    border: 1.5px solid var(--red);
    border-radius: 6px;
    text-align: center;
    color: var(--red);
    font-weight: 700;
    font-size: 16px;
    letter-spacing: .5px;
  }
  .servings {
    position: absolute;
    left: 0; right: 0;
    top: 374px;
    text-align: center;
    font-weight: 700;
    font-size: 13px;
    color: var(--ink);
  }
  .origin {
    position: absolute;
    left: 0; right: 0;
    top: 428px;
    text-align: center;
    font-weight: 800;
    font-size: 15px;
    color: var(--ink);
  }
  .net-weight {
    position: absolute;
    left: 14px;
    top: 412px;
    font-family: "Oswald", "Arial Narrow", sans-serif;
    font-weight: 500;
    font-size: 10px;
    line-height: 11px;
    color: var(--yellow);
  }
  .flavor {
    position: absolute;
    left: 266px;
    top: 379px;
    width: 60px;
    height: 60px;
    box-sizing: border-box;
    border: 3px solid var(--white);
    border-radius: 50%;
    background: var(--red);
    color: var(--white);
    font-weight: 700;
    font-size: 12px;
    line-height: 12px;
    display: flex;
    align-items: center;
    justify-content: center;
    text-align: center;
  }
</style>
</head>
<body>
<main class="canvas">

  <section class="label label--inline" aria-label="Label option with single-line brand name">
    <div class="label__stripe"></div>
    <h1 class="brand">VoltaRush</h1>
    <div class="label__lower"></div>
    <div class="compound">Beta-hydroxybutyrates (BHB)</div>
    <h2 class="title">KETONE SUPPLEMENT</h2>
    <div class="category">DIETARY SUPPLIMENT</div>
    <div class="servings">- 30 Servings &nbsp;- 12g BHB</div>
    <div class="net-weight">40.OZ/<br>1KG NET</div>
    <div class="flavor">Orange<br>Mango</div>
    <div class="origin">MADE IN USA</div>
  </section>

  <section class="label label--stacked" aria-label="Label option with large brand name">
    <div class="label__stripe"></div>
    <h1 class="brand">VoltaRush</h1>
    <div class="label__lower"></div>
    <div class="compound">Beta-hydroxybutyrates (BHB)</div>
    <h2 class="title">KETONE SUPPLEMENT</h2>
    <div class="category">DIETARY SUPPLIMENT</div>
    <div class="servings">- 30 Servings &nbsp;- 12g BHB</div>
    <div class="net-weight">40.OZ/<br>1KG NET</div>
    <div class="flavor">Orange<br>Mango</div>
    <div class="origin">MADE IN USA</div>
  </section>

</main>
</body>
</html>
```